Rise To Go Further! - Marketing, Training, Managment for Multifamily Professionals

Flyer for training event. I have to be able to edit location, times, speakers, cost,
We will have 2 to 4 speakers for each event. Each event may have a different topic relating to the main topic (Marketing, Training, Management). The idea is to get as many people to open or pick up the fly and say "I have to attend" this seminar. We are the experts in the industry and want to portray this with the flyer. Each speaker will have a topic and a certain amount of time. Each topic will be different.
Updates

Project Deadline Extended
Reason: I apologize for the new design deadline. I've been traveling extensively for work and unable to view submissions. Currently I am not traveling and able to dedicate time to view all of the wonderful submissions. I'm looking forward to selecting one. Thank you all for your understanding.

Target Market(s)

Multifamily - Apartment Communities, Owners, Apartment Associations, Leasing Agents, Marketing Directors, Managers, Presidents,

Industry/Entity Type

Marketing

Colors

Designer to choose colors to be used in the design.

Requirements
Must have
• Editable flyer. I have to be able to edit; location, times/date, speaker, cost, description.
• Sponsored by Tovali Power attached Logo for TVP
Nice to have
• Spot for photo of each speaker (2-4) speaker

```html
<!DOCTYPE html>
<html lang="en">
<head>
<meta charset="utf-8">
<title>Training Event Flyer</title>
<link rel="stylesheet" href="https://fonts.googleapis.com/css2?family=Bebas+Neue&family=Arimo:wght@400;700&display=swap">
<style>
  :root {
    --backdrop: #3a3a3c;
    --paper: #ffffff;
    --navy: #0c3f72;
    --ink: #111111;
    --title-band: rgba(40, 40, 40, 0.72);
    --photo-dark: #4a4540;
    --photo-light: #a39b8f;
    --portrait-tone: #c9c9c9;
    --rule: #e3e3e3;
  }
  * { margin: 0; padding: 0; box-sizing: border-box; }
  html, body {
    width: 999px; height: 1200px; overflow: hidden;
    background: var(--backdrop);
  }
  .flyer {
    position: absolute; left: 104px; top: 54px;
    width: 792px; height: 1120px;
    background: var(--paper);
    overflow: hidden;
    font-family: "Arimo", Arial, sans-serif;
  }
  .hero-photo {
    position: absolute; left: 0; top: 0; width: 792px; height: 534px;
    background: linear-gradient(180deg, #d9d6cf 0%, #9b8d7c 30%, var(--photo-light) 55%, var(--photo-dark) 100%);
  }
  .title-band {
    position: absolute; left: 0; top: 46px; width: 792px; height: 133px;
    background: var(--title-band);
  }
  .event-title {
    position: absolute; left: 0; top: 46px; width: 792px; height: 133px;
    font-family: "Bebas Neue", Impact, sans-serif;
    font-size: 132px; line-height: 146px; letter-spacing: 1px;
    color: #fff; text-align: center;
  }
  .venue-photo {
    position: absolute; left: 505px; top: 381px;
    width: 244px; height: 244px; border-radius: 50%;
    border: 8px solid var(--backdrop);
    background: radial-gradient(circle at 50% 30%, #b6a79b 0%, #8b7c74 45%, #e8e6e2 75%, #cfcfcf 100%);
  }
  .speaker {
    position: absolute; width: 792px;
  }
  .speaker-portrait {
    position: absolute; width: 132px; height: 132px; border-radius: 50%;
    border: 4px solid var(--navy);
    background: radial-gradient(circle at 50% 40%, #f2f2f2 0%, var(--portrait-tone) 70%, #ffffff 71%);
  }
  .speaker-topic {
    position: absolute;
    font-size: 20px; font-weight: 700; color: var(--navy); line-height: 24px;
  }
  .speaker-text {
    position: absolute; width: 557px;
    font-size: 14.3px; line-height: 18.6px; color: var(--ink);
    text-align: justify;
  }
  .speaker-one { top: 601px; }
  .speaker-two { top: 756px; }
  .speaker-three { top: 911px; }
  .portrait-left { left: 35px; top: 0; }
  .portrait-right { left: 617px; top: 2px; }
  .text-right .speaker-topic { left: 190px; top: 2px; }
  .text-right .speaker-text { left: 190px; top: 34px; }
  .text-left .speaker-topic { left: 42px; top: 2px; }
  .text-left .speaker-text { left: 42px; top: 34px; }
  .footer-band {
    position: absolute; left: 0; top: 1062px;
  }
  .sponsor-label {
    position: absolute; left: 568px; top: 1066px;
    font-size: 15px; font-weight: 700; color: var(--ink);
  }
  .sponsor-box {
    position: absolute; left: 686px; top: 1035px; width: 77px; height: 77px;
    border-top: 1px solid var(--rule); border-bottom: 1px solid var(--rule);
  }
  .sponsor-name {
    position: absolute; left: 0; top: 22px; width: 70px;
    font-size: 24px; font-weight: 700; color: var(--ink); text-align: center;
  }
</style>
</head>
<body>
<main class="flyer">
  <div class="hero-photo" role="img" aria-label="Photo of attendees seated at tables watching a presenter in a training room"></div>
  <div class="title-band"></div>
  <h1 class="event-title">Training Event</h1>
  <div class="venue-photo" role="img" aria-label="Photo of a conference hall with microphones and water jugs on tables"></div>

  <section class="speaker speaker-one text-right">
    <div class="speaker-portrait portrait-left" role="img" aria-label="Speaker portrait"></div>
    <h2 class="speaker-topic">Lorem Ipsum</h2>
    <p class="speaker-text">Lorem Ipsum is simply dummy text of the printing and typesetting industry. Lorem Ipsum has been the industry's standard dummy text ever since the 1500s, when an unknown printer took a galley of type and scrambled it to make a type specimen book. It has survived not only five centuries, but also the leap into electronic typesetting, remaining essentially unchanged.</p>
  </section>

  <section class="speaker speaker-two text-left">
    <h2 class="speaker-topic">Lorem Ipsum</h2>
    <p class="speaker-text">Lorem Ipsum is simply dummy text of the printing and typesetting industry. Lorem Ipsum has been the industry's standard dummy text ever since the 1500s, when an unknown printer took a galley of type and scrambled it to make a type specimen book. It has survived not only five centuries, but also the leap into electronic typesetting, remaining essentially unchanged.</p>
    <div class="speaker-portrait portrait-right" role="img" aria-label="Speaker portrait"></div>
  </section>

  <section class="speaker speaker-three text-right">
    <div class="speaker-portrait portrait-left" role="img" aria-label="Speaker portrait"></div>
    <h2 class="speaker-topic">Lorem Ipsum</h2>
    <p class="speaker-text">Lorem Ipsum is simply dummy text of the printing and typesetting industry. Lorem Ipsum has been the industry's standard dummy text ever since the 1500s, when an unknown printer took a galley of type and scrambled it to make a type specimen book. It has survived not only five centuries, but also the leap into electronic typesetting, remaining essentially unchanged.</p>
  </section>

  <svg class="footer-band" width="792" height="58" viewBox="0 0 792 58" aria-hidden="true">
    <polygon points="0,0 495,0 521,58 0,58" fill="var(--navy)"/>
  </svg>
  <p class="sponsor-label">Sponsored by</p>
  <div class="sponsor-box">
    <span class="sponsor-name">TVP</span>
  </div>
</main>
</body>
</html>
```